New business card design to go with our new logo

just want an eye-catching business card to go with our new logo. We are open to double sided or single sided. Just want it to have the following info on it. Whatever layout you think looks best.

First and Last Name
Title
Phone 801-555-7392
Address 214 W. Cedar Lane Pleasant Grove UT 84062
Email thecrew@marloweskennelandtreat.example

```html
<!DOCTYPE html>
<html lang="en">
<head>
<meta charset="utf-8">
<title>Marlowe's Kennel &amp; Treat – Business Card</title>
<link rel="stylesheet" href="https://fonts.googleapis.com/css2?family=Josefin+Slab:wght@600;700&family=Nunito:wght@800&display=swap">
<style>
  :root {
    --page-bg: #e9ecef;
    --card-bg: #ffffff;
    --orange: #e0824a;
    --blue: #3f9bcf;
    --shadow: rgba(20, 30, 45, 0.18);
  }
  * { box-sizing: border-box; margin: 0; padding: 0; }
  html, body {
    width: 1200px;
    height: 789px;
    overflow: hidden;
    background: var(--page-bg);
  }
  .card {
    position: absolute;
    left: 80px;
    top: 97px;
    width: 1040px;
    height: 594px;
    background: var(--card-bg);
    box-shadow: 0 12px 40px var(--shadow);
    overflow: hidden;
  }
  .contact-list {
    position: absolute;
    left: 0;
    top: 0;
    width: 100%;
    height: 100%;
    list-style: none;
  }
  .contact-item {
    position: absolute;
    right: 534px;
    display: flex;
    align-items: center;
    gap: 28px;
    font-family: "Nunito", Arial, sans-serif;
    font-weight: 800;
    font-size: 19px;
    line-height: 1.3;
    color: var(--orange);
    text-align: right;
    transform: translateY(-50%);
  }
  .contact-item--phone { top: 178px; }
  .contact-item--address { top: 244px; }
  .contact-item--email { top: 310px; }
  .contact-icon {
    flex: none;
    width: 46px;
    height: 46px;
  }
  .divider {
    position: absolute;
    left: 600px;
    top: 82px;
    width: 2px;
    height: 250px;
    background: var(--blue);
  }
  .brand {
    position: absolute;
    left: 630px;
    top: 96px;
    width: 370px;
    display: flex;
    flex-direction: column;
    align-items: center;
    gap: 22px;
  }
  .brand-circle {
    width: 110px;
    height: 110px;
    border-radius: 50%;
    border: 8px solid var(--orange);
  }
  .brand-name {
    font-family: "Josefin Slab", Georgia, serif;
    font-weight: 700;
    font-size: 44px;
    line-height: 1.05;
    color: var(--orange);
    text-align: center;
  }
  .wave {
    position: absolute;
    left: 0;
    top: 0;
    width: 1040px;
    height: 594px;
  }
  .person {
    position: absolute;
    left: 96px;
    top: 398px;
  }
  .person-name {
    font-family: "Josefin Slab", Georgia, serif;
    font-weight: 600;
    font-size: 46px;
    color: var(--blue);
    line-height: 1.1;
  }
  .person-title {
    margin-top: 10px;
    font-family: "Nunito", Arial, sans-serif;
    font-weight: 800;
    font-size: 26px;
    color: var(--orange);
  }
</style>
</head>
<body>
  <main class="card">
    <ul class="contact-list">
      <li class="contact-item contact-item--phone">
        <span class="contact-text">801-555-7392</span>
      </li>
      <li class="contact-item contact-item--address">
        <span class="contact-text">214 W. Cedar Lane<br>Pleasant Grove UT 84062</span>
      </li>
      <li class="contact-item contact-item--email">
        <span class="contact-text">thecrew@marloweskennelandtreat.example</span>
      </li>
    </ul>

    <svg class="wave" viewBox="0 0 1040 594" aria-hidden="true">
      <!-- contact icons -->
      <g class="icon-phone" transform="translate(540 178)" fill="none" stroke="var(--blue)" stroke-width="2.5">
        <circle r="23"/>
        <path d="M-11 -3 Q0 -10 11 -3 L9 1 L5 0 L4 -3 Q0 -5 -4 -3 L-5 0 L-9 1 Z" fill="var(--blue)" stroke="none"/>
        <rect x="-9" y="2" width="18" height="10" rx="2" fill="var(--blue)" stroke="none"/>
      </g>
      <g class="icon-pin" transform="translate(540 244)" fill="none" stroke="var(--blue)" stroke-width="2.5">
        <circle r="23"/>
        <path d="M0 13 C-4 6 -9 1 -9 -4 A9 9 0 0 1 9 -4 C9 1 4 6 0 13 Z"/>
        <circle cy="-4" r="3"/>
      </g>
      <g class="icon-email" transform="translate(540 310)" fill="none" stroke="var(--blue)" stroke-width="2.5">
        <circle r="23"/>
        <circle r="5"/>
        <path d="M5 -5 V3 Q5 7 8 7 Q12 7 12 0 A12 12 0 1 0 5 11"/>
      </g>
      <!-- flowing bands -->
      <path d="M0 392 C150 366 300 352 420 378 C530 402 580 488 690 488 C800 488 900 440 1040 430" fill="none" stroke="var(--orange)" stroke-width="9"/>
      <path d="M0 378 C150 352 300 338 420 364 C530 388 580 474 690 474 C800 474 900 426 1040 416" fill="none" stroke="var(--blue)" stroke-width="13"/>
    </svg>

    <div class="divider"></div>

    <div class="brand">
      <div class="brand-circle"></div>
      <div class="brand-name">Marlowe's<br>Kennel &amp; Treat</div>
    </div>

    <div class="person">
      <h1 class="person-name">Dana Whitfield</h1>
      <p class="person-title">- CEO</p>
    </div>
  </main>
</body>
</html>
```